Minimalist Sign Design (24” X 24”)

I am wanting to redesign our yard signs to be very clean, attractive, eye catching, and readable (imagine driving by a home with a sign In yard). We paint homes. I am hoping to have a design that incorporates our brand colors in a clean, professional way that represents our company. Clean, concise, easily read from a distance.

Target Market(s)

Homeowners

Industry/Entity Type

Painting And Decorating

Font styles to use
Sans Serif

Requirements
Must have
• Phone Number: (555) 014-7391
• Free Consultations
• Makeover in progress!
• Brand colors:
• Hunter Green: #355e3b
• Black
• White
Nice to have
• Would like the hunter green to he background color of sign. Can make logo white to stand out with the green.
Should not have
• Too busy or unable to read text

```html
<!DOCTYPE html>
<html lang="en">
<head>
<meta charset="utf-8">
<title>Summit Painting Yard Sign</title>
<link rel="stylesheet" href="https://fonts.googleapis.com/css2?family=Bebas+Neue&family=Saira:wght@700&display=swap">
<style>
  :root {
    --hunter-green: #355e3b;
    --sign-black: #000000;
    --ink-white: #ffffff;
    --backdrop: #eef0ec;
  }
  html, body {
    margin: 0;
    padding: 0;
    width: 1200px;
    height: 881px;
    overflow: hidden;
    background: var(--backdrop);
  }
  .canvas {
    width: 1200px;
    height: 881px;
    display: flex;
    align-items: center;
    justify-content: center;
  }
  .yard-sign {
    width: 841px;
    height: 841px;
    display: block;
  }
  .sign-panel { fill: var(--sign-black); }
  .check-mark {
    fill: none;
    stroke: var(--hunter-green);
    stroke-width: 4;
    stroke-linecap: round;
    stroke-linejoin: round;
  }
  .header-item {
    font-family: "Bebas Neue", sans-serif;
    font-size: 50px;
    fill: var(--ink-white);
  }
  .brand-disc { fill: var(--hunter-green); }
  .brand-name {
    font-family: "Bebas Neue", sans-serif;
    font-size: 96px;
    letter-spacing: 4px;
    fill: var(--ink-white);
  }
  .phone-number {
    font-family: "Saira", sans-serif;
    font-weight: 700;
    font-size: 92px;
    fill: var(--ink-white);
  }
</style>
</head>
<body>
<main class="canvas">
  <svg class="yard-sign" viewBox="0 0 873 873" xmlns="http://www.w3.org/2000/svg" aria-label="Summit Painting yard sign">
    <rect class="sign-panel" x="0" y="0" width="873" height="873"/>

    <g class="sign-header">
      <path class="check-mark" d="M45 60 L58 80 L80 34"/>
      <text class="header-item" x="85" y="83" textLength="316" lengthAdjust="spacingAndGlyphs">FREE CONSULTATIONS</text>
      <path class="check-mark" d="M435 60 L448 80 L470 34"/>
      <text class="header-item" x="473" y="83" textLength="362" lengthAdjust="spacingAndGlyphs">MAKEOVER IN PROGRESS</text>
    </g>

    <g class="brand-block">
      <circle class="brand-disc" cx="437" cy="436" r="322"/>
      <text class="brand-name" text-anchor="middle" x="437">
        <tspan x="437" y="420">SUMMIT</tspan>
        <tspan x="437" y="520">PAINTING</tspan>
      </text>
    </g>

    <text class="phone-number" x="437" y="848" text-anchor="middle" textLength="620" lengthAdjust="spacingAndGlyphs">(555) 014-7391</text>
  </svg>
</main>
</body>
</html>
```